Business Card Design Project

Card should be standard size
Logo placed in upper right corner and slogan upper left corner
English Name of company in middle under that Chinese name
Office address across bottom of card including phone number
My Name and title

Target Market(s)

Start-ups and small to medium size businesses
age 30-55

Industry/Entity Type

Business

Font styles to use
Sans Serif

Colors
ffffff

```html
<!DOCTYPE html>
<html lang="en">
<head>
<meta charset="utf-8">
<title>Business Card</title>
<link rel="stylesheet" href="https://fonts.googleapis.com/css2?family=Jost:wght@400;500&family=Noto+Sans:wght@400&display=swap">
<style>
  :root {
    --ink-deep: #141414;
    --ink-panel: #1c1c1c;
    --white: #ffffff;
    --lime: #99f200;
    --rule-dark: #9c9c9c;
    --rule-light: #e2e2e2;
    --display: "Jost", "Century Gothic", sans-serif;
    --body: "Noto Sans", "Open Sans", sans-serif;
  }
  * { margin: 0; padding: 0; box-sizing: border-box; }
  html, body { width: 1200px; height: 720px; overflow: hidden; background: var(--ink-deep); }
  .card {
    position: relative;
    width: 1200px;
    height: 720px;
    background: var(--ink-deep);
    color: var(--white);
    overflow: hidden;
  }
  .slogan {
    position: absolute;
    left: 87px;
    top: 128px;
    font-family: var(--display);
    font-weight: 500;
    font-size: 42px;
    line-height: 1;
    letter-spacing: -0.5px;
  }
  .brand {
    position: absolute;
    right: 80px;
    top: 81px;
    width: 178px;
    display: flex;
    flex-direction: column;
    align-items: center;
  }
  .brand-mark {
    width: 118px;
    height: 118px;
    border-radius: 14px;
    background: var(--lime);
  }
  .brand-name {
    margin-top: 6px;
    font-family: var(--display);
    font-weight: 400;
    font-size: 40px;
    line-height: 1;
    white-space: nowrap;
  }
  .company-name {
    position: absolute;
    left: 0;
    width: 1275px;
    top: 249px;
    text-align: center;
    font-family: var(--display);
    font-weight: 500;
    font-size: 85px;
    line-height: 1;
    letter-spacing: 0.5px;
  }
  .contact-panel {
    position: absolute;
    left: 0;
    top: 432px;
    width: 1200px;
    height: 168px;
    background: var(--ink-panel);
  }
  .address, .phones {
    position: absolute;
    top: 46px;
    font-family: var(--body);
    font-size: 22.5px;
    line-height: 43px;
    letter-spacing: 0.6px;
    white-space: nowrap;
  }
  .address { left: 113px; }
  .phones { left: 919px; }
  .icon {
    position: absolute;
    fill: var(--lime);
  }
  .icon-pin { left: -34px; top: 10px; width: 20px; height: 28px; }
  .icon-phone { left: -38px; top: 11px; width: 16px; height: 24px; }
  .icon-fax { left: -44px; top: 54px; width: 24px; height: 24px; }
  .holder {
    position: absolute;
    left: 406px;
    width: 400px;
    top: 42px;
    text-align: center;
    font-family: var(--display);
  }
  .holder-name { font-size: 48px; font-weight: 400; line-height: 1; letter-spacing: -0.5px; }
  .holder-title { margin-top: 7px; font-size: 24px; line-height: 1; }
  .rule-dark { position: absolute; left: 0; top: 600px; width: 1200px; height: 13px; background: var(--rule-dark); }
  .rule-light { position: absolute; left: 0; top: 613px; width: 1200px; height: 15px; background: var(--rule-light); }
  .lime-band { position: absolute; left: 0; top: 628px; width: 1200px; height: 92px; background: var(--lime); }
</style>
</head>
<body>
  <main class="card">
    <p class="slogan">Your Slogen</p>

    <div class="brand">
      <div class="brand-mark"></div>
      <p class="brand-name">Your Logo</p>
    </div>

    <h1 class="company-name">Compney Name</h1>

    <section class="contact-panel">
      <div class="address">
        <svg class="icon icon-pin" viewBox="0 0 20 28" aria-hidden="true">
          <path d="M10 0C4.5 0 0 4.4 0 9.8 0 17 10 28 10 28s10-11 10-18.2C20 4.4 15.5 0 10 0zm0 14a4.3 4.3 0 1 1 0-8.6 4.3 4.3 0 0 1 0 8.6z"/>
        </svg>
        <p>218 Maple Ridge Ave,</p>
        <p>Brookhaven NY 40217</p>
      </div>

      <div class="holder">
        <p class="holder-name">Your Name</p>
        <p class="holder-title">Your Title</p>
      </div>

      <div class="phones">
        <svg class="icon icon-phone" viewBox="0 0 16 24" aria-hidden="true">
          <path d="M5 0h3.5l1 6.5L6.8 8c-.4 2.6.2 5.5 1.8 8l3-1 3.2 5.5L11.5 23C5.5 24 1 13 3 3.5 3.3 1.5 4 .3 5 0z"/>
        </svg>
        <svg class="icon icon-fax" viewBox="0 0 24 24" aria-hidden="true">
          <path d="M5 0h14v9h-2V2H7v7H5zM9 4h6v1.6H9zm0 3h6v1.6H9zM1 10h22v14H1zm2 2v4h18v-4zm0 6v4h18v-4z"/>
        </svg>
        <p>+(000) 5550 1428</p>
        <p>+(000) 5550 1429</p>
      </div>
    </section>

    <div class="rule-dark"></div>
    <div class="rule-light"></div>
    <div class="lime-band"></div>
  </main>
</body>
</html>
```